Holvern Incorporated

Holvern is a business that provides consulting, and manages and supplies trades persons in the construction and heavy industries sector. We build, do maintenance, install machinery, and can manage projects or jobs. Would like or prefer more clean, classic designs. Blacks/greys, but open to almost anything.

Target Market(s)

Industrial/Construction/Manufacturing

Industry/Entity Type

Construction Company

Contact Information for Business Card

Clean, business name on the front, possibly have the details on the back, but open to any ideas.

Logo Text

We currently do not have a slogan, open to ideas

Font styles to use
Serif
Sans Serif

Colors

Designer to choose colors to be used in the design.

Requirements
Should not have
• the oval is not my logo, was just an idea. please don't send 20 designs with the oval

```html
<!DOCTYPE html>
<html lang="en">
<head>
<meta charset="utf-8">
<title>Holvern Incorporated — Business Card</title>
<link href="https://fonts.googleapis.com/css2?family=Roboto+Slab:wght@700&family=Oswald:wght@500&family=Roboto:wght@400&display=swap" rel="stylesheet">
<style>
  :root {
    --backdrop: #6e6e6e;
    --card-light: #ffffff;
    --card-dark: #2b2b2d;
    --ink-dark: #3a3a3c;
    --ink-light: #ffffff;
    --ink-muted: #d8d8d8;
    --rule-light: #ffffff;
  }
  * { box-sizing: border-box; margin: 0; padding: 0; }
  html, body {
    width: 1200px; height: 1200px; overflow: hidden;
    background: var(--backdrop);
  }
  .stage {
    width: 1200px; height: 1200px;
    display: flex; flex-direction: column; align-items: center; justify-content: center;
    gap: 70px;
  }
  .card {
    position: relative;
    width: 700px; height: 400px;
    box-shadow: 0 10px 30px rgba(0,0,0,0.25);
  }
  .card--front {
    background: var(--card-light);
    display: flex; align-items: center; justify-content: center;
  }
  .card--back { background: var(--card-dark); }

  .wordmark {
    display: flex; align-items: center; gap: 14px;
    font-family: "Roboto Slab", Georgia, serif;
    font-weight: 700;
    letter-spacing: 0.5px;
    white-space: nowrap;
  }
  .wordmark__mark { display: block; flex: none; }
  .card--front .wordmark { font-size: 50px; color: var(--ink-dark); }
  .card--front .wordmark__mark { width: 30px; height: 30px; background: var(--ink-dark); }

  .card--back .wordmark {
    position: absolute; left: 60px; top: 232px;
    font-size: 26px; color: var(--ink-light);
  }
  .card--back .wordmark__mark { width: 16px; height: 16px; background: var(--ink-light); }

  .connector {
    position: absolute; left: 60px; top: 214px;
    width: 340px; height: 2px;
  }

  .details {
    position: absolute; right: 60px; top: 60px;
    width: 240px;
    text-align: right; color: var(--ink-light);
    font-family: "Roboto", Arial, sans-serif;
  }
  .details__name {
    font-family: "Oswald", "Arial Narrow", sans-serif;
    font-weight: 500; font-size: 26px; letter-spacing: 1px; line-height: 1.1;
  }
  .details__role {
    font-size: 15px; letter-spacing: 1.5px; color: var(--ink-muted);
    margin-top: 2px; padding-bottom: 6px;
    border-bottom: 1px solid var(--rule-light);
    margin-left: 80px;
  }
  .details__address { margin-top: 22px; font-size: 16px; line-height: 1.45; }
  .details__contact { margin-top: 14px; font-size: 16px; line-height: 1.45; }
</style>
</head>
<body>
<main class="stage">
  <section class="card card--front" aria-label="Card front">
    <div class="wordmark">
      <span class="wordmark__mark" aria-hidden="true"></span>
      <span class="wordmark__name">Holvern Incorporated</span>
    </div>
  </section>

  <section class="card card--back" aria-label="Card back">
    <svg class="connector" viewBox="0 0 340 2" preserveAspectRatio="none" aria-hidden="true">
      <line x1="0" y1="1" x2="340" y2="1" stroke="var(--rule-light)" stroke-width="2"/>
    </svg>
    <div class="wordmark">
      <span class="wordmark__mark" aria-hidden="true"></span>
      <span class="wordmark__name">Holvern Incorporated</span>
    </div>
    <div class="details">
      <p class="details__name">YOUR NAME</p>
      <p class="details__role">JOB POSITION</p>
      <p class="details__address">2364 First Address Line<br>Second Address Line,56324</p>
      <p class="details__contact">+0 123 456 7899<br>lorem@ipsum.com<br>websitename.com</p>
    </div>
  </section>
</main>
</body>
</html>
```